"When Grapes Remember" Book Cover Design

I need a design for the cover of a book I have written. I'm attaching the lead into the book to help provide context for you. I want the cover to be unique and outside of the box while still staying in line with the energy and feel of the content.

"Wine always had a way of speaking to me, even if I didn’t quite understand what it was saying. Upon making a decision to spend my life pursuing wine, I began to hear it loud and clear. I knew it had to be more than rich man’s drink, lifestyle trend, or just frivolous alcohol. I resolved it had a deeper meaning. In the years of trying to understand wine’s whole story, it ended up crafting mine.
When Grapes Remember is the intertwining of two personal stories, one about wine and one about myself. My goal is to tell wine’s story in tandem with my own. In this way, I can give wine the authentic voice it deserves. I want you to learn about wine like I learned, little by little. Each Wine 101 chapter seeks to answer the most common questions and misconceptions I have encountered with wine throughout the years. Every wine chapter will give you a foundation to build on, more confidence, and a greater love for wine."

Thank you for your time!

Target Market(s)

Men and Women Wine Lovers between the ages of 25-50

Colors

Designer to choose colors to be used in the design.

Requirements
Must have
• An eye catching appeal. Connect the title with the contents and convey the spirit of the book. A way to showcase the contents without being overly obvious and still having some mystery to the contents. Invite the potential reader to look deeper.

```html
<!DOCTYPE html>
<html lang="en">
<head>
<meta charset="utf-8">
<title>When Grapes Remember – Book Cover</title>
<link rel="stylesheet" href="https://fonts.googleapis.com/css2?family=Cinzel:wght@400;500&family=Cormorant+Garamond:ital,wght@1,500&display=swap">
<style>
  :root {
    --page-bg: #f4f4f4;
    --plum-deep: #220c3b;
    --plum-mid: #3a1a58;
    --plum-glow: #5a2a80;
    --gold-light: #f0d48a;
    --gold: #d4a94e;
    --gold-dark: #b8862f;
    --ivory: #f2f0f4;
  }
  * { margin: 0; padding: 0; box-sizing: border-box; }
  html, body {
    width: 1200px;
    height: 1108px;
    overflow: hidden;
    background: var(--page-bg);
  }
  .book-cover {
    position: absolute;
    left: 280px;
    top: 74px;
    width: 640px;
    height: 960px;
    background: radial-gradient(ellipse 60% 45% at 50% 50%, var(--plum-glow) 0%, var(--plum-mid) 55%, var(--plum-deep) 100%);
    box-shadow: 0 10px 30px rgba(0,0,0,0.18);
    text-align: center;
  }
  .ornament {
    position: absolute;
    left: 200px;
    width: 240px;
    background: radial-gradient(ellipse at center, var(--gold) 0%, rgba(212,169,78,0.35) 55%, rgba(212,169,78,0) 75%);
    opacity: 0.85;
  }
  .ornament--top { top: 188px; height: 82px; }
  .ornament--bottom { top: 680px; height: 60px; }
  .rules { position: absolute; left: 0; top: 0; }
  .title {
    position: absolute;
    left: 0;
    width: 100%;
    font-family: "Cinzel", serif;
    font-weight: 400;
    line-height: 1;
    background: linear-gradient(100deg, var(--gold-dark) 0%, var(--gold-light) 45%, var(--gold) 70%, var(--gold-dark) 100%);
    -webkit-background-clip: text;
    background-clip: text;
    color: transparent;
  }
  .title__first { top: 300px; font-size: 132px; letter-spacing: 0.02em; }
  .title__middle {
    position: absolute;
    left: 0;
    width: 100%;
    top: 440px;
    font-family: "Cormorant Garamond", serif;
    font-style: italic;
    font-weight: 500;
    font-size: 62px;
    line-height: 1;
    color: var(--ivory);
  }
  .title__last { top: 520px; font-size: 92px; letter-spacing: -0.01em; }
  .author-name {
    position: absolute;
    left: 0;
    width: 100%;
    top: 842px;
    font-family: "Cinzel", serif;
    font-weight: 400;
    font-size: 30px;
    letter-spacing: 0.12em;
    color: var(--ivory);
  }
</style>
</head>
<body>
  <main class="book-cover">
    <svg class="rules" width="640" height="960" viewBox="0 0 640 960" aria-hidden="true">
      <g stroke="#c99a45" stroke-width="1.2">
        <line x1="58" y1="252" x2="190" y2="252"/>
        <line x1="450" y1="252" x2="582" y2="252"/>
        <line x1="58" y1="710" x2="190" y2="710"/>
        <line x1="450" y1="710" x2="582" y2="710"/>
      </g>
    </svg>
    <div class="ornament ornament--top" role="img" aria-label="Gold wine glass above a flourish of grape leaves and scrolls"></div>
    <h1>
      <span class="title title__first">WHEN</span>
      <span class="title__middle">grapes</span>
      <span class="title title__last">REMEMBER</span>
    </h1>
    <div class="ornament ornament--bottom" role="img" aria-label="Gold flourish of grape leaves and scrolls"></div>
    <p class="author-name">AUTHOR’S NAME</p>
  </main>
</body>
</html>
```